Business Card Design - Furniture Retail

Open to both Single or double sided design

We are launching a online ecommerce store that sells Scandinavian/Danish style of furniture in Australia.

We aspire to provide stylish but classic and designers' selection of furniture to the Australia public at affordable price. For the style of the furniture we are selling, please see the following links:

https://www.boxlyshare.com/sh/qrk7vz2mwpl04tn/BBXTpeLr3h52Kd7nWqYzRsGmu?dl=0

The style of the design we are looking for is clean, simple that look Scandinavian/Danish but yet it is timeless classic.

Aspiring Design
http://www.hallwick.com
http://brenlowe.com.au/
http://kolvo.furniture/
http://www.tipo.com/
Updates

Please display the card on normal angle for both front and back instead of funny angle. Please keep it display when displaying the design of the business cards so that we can focus on the designs rather than being confused by the unnecessary stuffs like the hands or background

I think there is already enough curve line on the logo itself so anything extra of the curve on the business card would be really unnecessary. Please avoid using any of the extra curve line on the business card, other than the logo itself. Thanks

Regular card and give them a matt celloglaze to create texture on card that makes it looked luxury and expensive.

Please display design on normal angle! Please only use white colour in the background (not the business card but the referring to the submission) rather than anything fancy so that we can focus on the design.

Target Market(s)

High end market consumers who are financially capable and who has good taste and appreciate good design

aged between 28 - 45 white collars professional/businessmen who live in metropolitan areas

Industry/Entity Type

Business

Font styles to use
Serif
Sans Serif

Requirements
Must have
• Regular card and give them a matt celloglaze to create texture on card that makes it looked luxury and expensive.

Please use the logo from the uploaded files

Company Name: Miles Orveda
Name: Peter Holm
Phone: +614 27 505 316
Website: www.milesorveda.com.au
Email: peter@milesorveda.com.au
Nice to have
• Colour is not limited to black and white
Should not have
• The concept photos of the furniture should NOT be used in the FRONT page of the business card.

```html
<!DOCTYPE html>
<html lang="en">
<head>
<meta charset="utf-8">
<title>Miles Orveda — Business Card</title>
<link rel="stylesheet" href="https://fonts.googleapis.com/css2?family=Cinzel:wght@500&family=Tinos&display=swap">
<style>
  :root {
    --page: #ffffff;
    --card-front: #f4f4f3;
    --card-back: #1c1c1c;
    --ink: #1a1a1a;
    --icon: #a3a3a3;
    --emboss: #262626;
    --edge: #e2e2e0;
  }
  html, body {
    margin: 0;
    padding: 0;
    width: 1200px;
    height: 900px;
    overflow: hidden;
    background: var(--page);
  }
  .canvas {
    position: relative;
    width: 1200px;
    height: 900px;
  }
  .card {
    position: absolute;
    left: 354px;
    width: 488px;
    height: 279px;
    box-sizing: border-box;
  }
  .card-front {
    top: 153px;
    background: var(--card-front);
    border: 1px solid var(--edge);
  }
  .card-back {
    top: 463px;
    background: var(--card-back);
  }
  .brand-name {
    position: absolute;
    left: 49px;
    top: 50px;
    margin: 0;
    font-family: "Cinzel", serif;
    font-weight: 500;
    font-size: 25px;
    letter-spacing: 0.5px;
    color: var(--ink);
    line-height: 1;
  }
  .person-name {
    position: absolute;
    left: 49px;
    top: 126px;
    margin: 0;
    font-family: "Cinzel", serif;
    font-weight: 500;
    font-size: 20px;
    color: var(--ink);
    line-height: 1;
  }
  .contact-list {
    position: absolute;
    left: 49px;
    top: 176px;
    margin: 0;
    padding: 0;
    list-style: none;
    font-family: "Tinos", serif;
    font-size: 15px;
    color: var(--ink);
  }
  .contact-list li {
    display: flex;
    align-items: center;
    height: 20.5px;
  }
  .contact-list svg {
    width: 12px;
    height: 12px;
    margin-right: 12px;
    fill: var(--icon);
    flex: none;
  }
  .back-brand {
    position: absolute;
    left: 0;
    right: 0;
    top: 120px;
    margin: 0;
    text-align: center;
    font-family: "Cinzel", serif;
    font-weight: 500;
    font-size: 40px;
    letter-spacing: 1px;
    color: var(--emboss);
    line-height: 1;
  }
</style>
</head>
<body>
<main class="canvas">
  <section class="card card-front" aria-label="Card front">
    <p class="brand-name">Miles Orveda</p>
    <p class="person-name">Peter Holm</p>
    <ul class="contact-list">
      <li>
        <svg viewBox="0 0 12 12" aria-hidden="true"><path d="M2.3 0.8l1.8 1.9-1 1.3c0.8 1.8 2.1 3.2 3.9 4l1.3-1 1.9 1.8-1.1 1.9c-4.3-0.6-7.4-3.7-8-8z"/></svg>
        <span>+614 27 505 316</span>
      </li>
      <li>
        <svg viewBox="0 0 12 12" aria-hidden="true"><path d="M0 2.5h12v7H0z M0.8 3.2v0.4L6 6.8l5.2-3.2v-0.4z" fill-rule="evenodd"/></svg>
        <span>peter@milesorveda.com.au</span>
      </li>
      <li>
        <svg viewBox="0 0 12 12" aria-hidden="true"><circle cx="6" cy="6" r="5.6"/><path d="M6 1.2c-1.4 1.2-2 3-2 4.8s0.6 3.6 2 4.8M6 1.2c1.4 1.2 2 3 2 4.8s-0.6 3.6-2 4.8M1.2 6h9.6" stroke="#f4f4f3" stroke-width="0.8" fill="none"/></svg>
        <span>www.milesorveda.com.au</span>
      </li>
    </ul>
  </section>
  <section class="card card-back" aria-label="Card back">
    <p class="back-brand">Miles Orveda</p>
  </section>
</main>
</body>
</html>
```